Postcard Handout

We need a postcard to market university fairs in Southeast Asia. The fairs are organized by LearnBridgeAbroad which is a program of the Federal Bureau of Outreach http://ocp.outreachbureau.example/learnbridgeabroad/

The audience for these postcards are U.S. higher education recruiters (not students). We want U.S. universities to sign up for the fairs.

The postcards will be handed out at large education conferences.

Target Market(s)

U.S. university recruiters who are between the ages of 25 and 45.

Industry/Entity Type

University

Requirements
Must have

• Copy/Text: Please see attached doc. file for copy/text to be used on the front and back of the card.

Front: High color gloss

Back: Black and white only design

Featured Colors: Red, White, and Blue
- Should have a patriotic / U.S. government feel

Logos: Must use the Outreach Bureau logo and at least one LearnBridgeAbroad logo (can use more but not required)
Nice to have
• -

```html
<!DOCTYPE html>
<html lang="en">
<head>
<meta charset="utf-8">
<title>2015 Southeast Asia Fair Series – Postcard</title>
<link rel="stylesheet" href="https://fonts.googleapis.com/css2?family=Fira+Sans:wght@400;500&display=swap">
<style>
  :root{
    --navy:#0f1f5c;
    --navy-deep:#0a1748;
    --flag-red:#b0171f;
    --brand-red:#c4163a;
    --brand-blue:#1b3f6e;
    --sky:#e9ecf1;
    --grey-top:#f4f4f4;
    --grey-mid:#d3d3d3;
    --ink:#111111;
    --paper:#ffffff;
    --stamp:#8c8c8c;
  }
  *{box-sizing:border-box;margin:0;padding:0}
  html,body{width:1200px;height:1000px;overflow:hidden;background:var(--paper)}
  body{position:relative;font-family:"Fira Sans",Arial,sans-serif;color:var(--ink)}

  .card{position:absolute;background:var(--paper);box-shadow:2px 3px 6px rgba(0,0,0,.45)}
  .card--front{left:8px;top:5px;width:1190px;height:487px;overflow:hidden;
    background:linear-gradient(180deg,var(--grey-top) 0%,var(--grey-mid) 30%,var(--sky) 100%)}
  .card--back{left:0;top:500px;width:1198px;height:495px}

  .front-wave{position:absolute;left:0;top:0;width:1190px;height:487px}

  .brand-box{position:absolute;left:30px;top:15px;width:288px;height:127px;background:var(--paper);
    display:flex;align-items:center;justify-content:center;gap:8px}
  .brand-name{font-size:26px;font-weight:500;color:var(--brand-red)}
  .brand-dot{width:12px;height:12px;border-radius:50%;background:var(--brand-blue)}
  .graduate-photo{position:absolute;left:318px;top:15px;width:251px;height:127px;
    background:linear-gradient(135deg,#cfd8c4 0%,#7d8a72 45%,#1e1e22 100%)}

  .agency-mark{position:absolute;left:822px;top:0;width:230px;height:148px;display:flex;
    flex-direction:column;align-items:center;justify-content:center;gap:8px}
  .agency-circle{width:70px;height:70px;border-radius:50%;border:3px solid #555}
  .agency-name{font-size:19px;color:#444;text-align:center}

  .front-copy{position:absolute;left:0;top:228px;width:1190px;text-align:center;color:var(--paper)}
  .front-title{font-size:27px;font-weight:400;line-height:32px}
  .country-list{list-style:none;margin-top:8px;font-size:18px;line-height:21.5px}
  .newsletter{position:absolute;left:8px;top:432px;font-size:19px;color:var(--paper)}

  .partner-strip{position:absolute;left:0;top:462px;width:1190px;height:25px;background:var(--paper);
    display:flex;align-items:center}
  .partner{position:absolute;top:4px;height:17px;background:#c9cfe0;border-radius:2px}
  .partner--seal{left:92px;width:26px;border-radius:50%}
  .partner--a{left:310px;width:90px;border-radius:50%;background:#aeb8d6}
  .partner--b{left:556px;width:196px;background:#b7bfd8}
  .partner--c{left:910px;width:190px;background:#c8d4e6}

  .dates-banner{position:absolute;left:6px;top:17px;width:591px;height:81px;background:var(--ink);
    border-radius:9px;color:var(--paper);text-align:center;padding-top:5px}
  .dates-banner h2{font-size:29px;font-weight:400;line-height:34px}
  .dates-banner p{font-size:24px;line-height:28px}

  .schedule{position:absolute;left:0;top:105px;width:604px;list-style:none;text-align:center;
    font-size:19px;line-height:23.2px}

  .contact-bar{position:absolute;left:6px;top:449px;width:600px;height:28px;background:var(--ink);
    border-radius:7px;color:var(--paper);font-size:19px;line-height:28px;text-align:center}

  .back-brand{position:absolute;left:632px;top:30px;width:170px;display:flex;flex-direction:column;
    align-items:center;gap:8px}
  .back-brand .brand-name{font-size:22px}

  .stamp-box{position:absolute;left:1005px;top:20px;width:152px;height:92px;border:2px solid var(--stamp)}
</style>
</head>
<body>

<section class="card card--front" aria-label="Postcard front">
  <svg class="front-wave" viewBox="0 0 1190 487" aria-hidden="true">
    <path d="M0 140 C300 150 700 175 1190 100 L1190 487 L0 487 Z" fill="var(--flag-red)"/>
    <path d="M0 150 C300 160 700 182 1190 112 L1190 487 L0 487 Z" fill="var(--paper)"/>
    <path d="M0 158 C300 168 700 190 1190 122 L1190 487 L0 487 Z" fill="var(--navy)"/>
    <path d="M0 200 C350 240 800 215 1190 196 L1190 212 C800 232 350 252 0 214 Z" fill="var(--paper)" opacity=".85"/>
    <path d="M0 210 C350 250 800 226 1190 206 L1190 218 C800 238 350 260 0 222 Z" fill="var(--flag-red)"/>
    <rect x="0" y="228" width="1190" height="240" fill="var(--navy-deep)"/>
  </svg>

  <div class="brand-box">
    <span class="brand-dot"></span>
    <span class="brand-name">LearnBridgeAbroad</span>
  </div>
  <div class="graduate-photo" role="img" aria-label="Photo of a smiling graduate in cap and gown holding a diploma"></div>

  <div class="agency-mark">
    <span class="agency-circle"></span>
    <span class="agency-name">Federal Bureau of Outreach</span>
  </div>

  <div class="front-copy">
    <h1 class="front-title">Join us for the 2015 Southeast Asia Fair Series<br>January 21 – February 3</h1>
    <ul class="country-list">
      <li>Thailand</li><li>Malaysia</li><li>Vietnam</li><li>Burma</li><li>Cambodia</li><li>Brunei</li>
    </ul>
  </div>
  <p class="newsletter">Subscribe to our newsletter to receive updates lbabroad.example/FairUpdates</p>

  <div class="partner-strip" aria-label="Partner badges">
    <span class="partner partner--seal"></span>
    <span class="partner partner--a"></span>
    <span class="partner partner--b"></span>
    <span class="partner partner--c"></span>
  </div>
</section>

<section class="card card--back" aria-label="Postcard back">
  <div class="dates-banner">
    <h2>Save the dates!</h2>
    <p>10 Cities / 6 Countries</p>
  </div>

  <ul class="schedule">
    <li>Jan 21 (We) Mandalay</li>
    <li>Jan 22 (Th): Yangon</li>
    <li>Jan 23 (Fr): Chiang Mai</li>
    <li>Jan 24 (Sa): Bangkok</li>
    <li>Jan 25 (Su): Kuala Lumpur</li>
    <li>Jan 26 (Mo): Kuala Lumpur / Penang travel</li>
    <li>Jan 27 (Tu): Penang</li>
    <li>Jan 28 (We): Penang / HCMC travel</li>
    <li>Jan 29 (Th): Ho Chi Minh City</li>
    <li>Jan 30 (Fr): Hanoi</li>
    <li>Jan 31 (Sa): Hanoi / Phnom Penh travel</li>
    <li>Feb 1 (Su): Phnom Penh</li>
    <li>Feb 2 (Mo): Phnom Penh / Brunei travel</li>
    <li>Feb 3 (Tu): Brunei</li>
  </ul>

  <p class="contact-bar">Questions? Email SEAsiaFairs@learnbridgeabroad.example</p>

  <div class="back-brand">
    <span class="brand-dot"></span>
    <span class="brand-name">LearnBridgeAbroad</span>
  </div>

  <div class="stamp-box" aria-label="Stamp area"></div>
</section>

</body>
</html>
```